Torvaline business cards

Need fresh design for our business cards. Logo must be specific, we are open for everything else.

Contact Information for Business Card

phrase "GMP & JANITORIAL SERVICES" should be used as main point of card

Colors
3176b5
3276b5
85acd3
cedeed
ffffff
0292cd
33a6d7
85cae6
cee9f5

Requirements
Must have
• The logo
Should not have
• crowded designs

```html
<!DOCTYPE html>
<html lang="en">
<head>
<meta charset="utf-8">
<title>Torvaline business cards</title>
<link rel="stylesheet" href="https://fonts.googleapis.com/css2?family=Open+Sans:wght@400;600&display=swap">
<style>
  :root {
    --backdrop: #d4d4d4;
    --card-blue: #1b7cc1;
    --brand-blue: #3176b5;
    --accent-blue: #0292cd;
    --emboss: #4f97cf;
    --band: #d5e0ec;
    --divider: #85acd3;
    --ink: #2b2b2b;
    --paper: #ffffff;
  }
  * { margin: 0; padding: 0; box-sizing: border-box; }
  html, body { width: 1200px; height: 900px; overflow: hidden; }
  body {
    background: var(--backdrop);
    font-family: "Open Sans", Arial, sans-serif;
    display: flex;
    align-items: center;
    justify-content: center;
    gap: 60px;
  }
  .card {
    width: 520px;
    height: 297px;
    position: relative;
    overflow: hidden;
  }
  .brand {
    display: flex;
    flex-direction: column;
    align-items: center;
    gap: 4px;
  }
  .wordmark {
    display: flex;
    align-items: center;
    gap: 12px;
    font-weight: 400;
    letter-spacing: 0.14em;
    line-height: 1.2;
  }
  .wordmark-dot {
    border-radius: 50%;
    flex: none;
  }
  .tagline {
    font-size: 11px;
    font-weight: 400;
    letter-spacing: 0.24em;
    padding-left: 26px;
  }

  .card-front {
    background: var(--card-blue);
    display: flex;
    align-items: center;
    justify-content: center;
  }
  .card-front .wordmark { font-size: 38px; color: var(--emboss); }
  .card-front .wordmark-dot { width: 14px; height: 14px; background: var(--emboss); }
  .card-front .tagline { color: var(--emboss); }

  .card-back { background: var(--paper); }
  .card-back .brand {
    position: absolute;
    top: 38px;
    left: 0; right: 0;
  }
  .card-back .wordmark { font-size: 36px; color: var(--brand-blue); }
  .card-back .wordmark-dot { width: 12px; height: 12px; background: var(--brand-blue); }
  .card-back .tagline { color: var(--accent-blue); }

  .name-band {
    position: absolute;
    top: 126px;
    left: 0; right: 0;
    height: 72px;
    background: var(--band);
    text-align: center;
    padding-top: 14px;
  }
  .person-name {
    font-weight: 600;
    font-size: 19px;
    color: var(--brand-blue);
    line-height: 1.2;
  }
  .person-title {
    font-size: 14px;
    color: var(--ink);
  }
  .contact-row {
    position: absolute;
    left: 0; right: 0;
    bottom: 22px;
    display: flex;
    align-items: center;
    justify-content: space-around;
    padding: 0 20px;
  }
  .contact-item {
    display: flex;
    flex-direction: column;
    align-items: center;
    gap: 6px;
    font-size: 14px;
    color: var(--ink);
    width: 140px;
    white-space: nowrap;
  }
  .contact-icon { width: 22px; height: 22px; }
  .contact-divider {
    width: 1px;
    height: 34px;
    background: var(--divider);
  }
</style>
</head>
<body>
  <section class="card card-front" aria-label="Card front">
    <div class="brand">
      <div class="wordmark"><span class="wordmark-dot"></span><span>TORVALINE</span></div>
      <p class="tagline">GMP &amp; JANITORIAL SERVICES</p>
    </div>
  </section>

  <section class="card card-back" aria-label="Card back">
    <div class="brand">
      <div class="wordmark"><span class="wordmark-dot"></span><span>TORVALINE</span></div>
      <p class="tagline">GMP &amp; JANITORIAL SERVICES</p>
    </div>

    <div class="name-band">
      <p class="person-name">Daniel Reyes</p>
      <p class="person-title">Founder</p>
    </div>

    <div class="contact-row">
      <div class="contact-item">
        <svg class="contact-icon" viewBox="0 0 22 22" aria-hidden="true">
          <circle cx="11" cy="11" r="10" fill="none" stroke="var(--accent-blue)" stroke-width="1.5"/>
          <rect x="5.5" y="7.5" width="11" height="7" fill="none" stroke="var(--accent-blue)" stroke-width="1.3"/>
          <path d="M5.5 7.5 L11 12 L16.5 7.5" fill="none" stroke="var(--accent-blue)" stroke-width="1.3"/>
        </svg>
        <span>info@torvaline.ca</span>
      </div>
      <span class="contact-divider"></span>
      <div class="contact-item">
        <svg class="contact-icon" viewBox="0 0 22 22" aria-hidden="true">
          <circle cx="11" cy="11" r="10" fill="none" stroke="var(--accent-blue)" stroke-width="1.5"/>
          <path d="M7.5 6.5 L9.5 6.5 L10.3 9 L9 10 Q10 12.5 12 13 L13 11.7 L15.5 12.5 L15.5 14.5 Q11 15.5 8.5 12 Q6.5 9.5 7.5 6.5 Z" fill="var(--accent-blue)"/>
        </svg>
        <span>1 (866) 555-0147</span>
      </div>
      <span class="contact-divider"></span>
      <div class="contact-item">
        <svg class="contact-icon" viewBox="0 0 22 22" aria-hidden="true">
          <circle cx="11" cy="11" r="10" fill="none" stroke="var(--accent-blue)" stroke-width="1.5"/>
          <circle cx="11" cy="11" r="5.5" fill="none" stroke="var(--accent-blue)" stroke-width="1.1"/>
          <ellipse cx="11" cy="11" rx="2.3" ry="5.5" fill="none" stroke="var(--accent-blue)" stroke-width="1.1"/>
          <path d="M5.5 11 H16.5" stroke="var(--accent-blue)" stroke-width="1.1"/>
        </svg>
        <span>www.torvaline.ca</span>
      </div>
    </div>
  </section>
</body>
</html>
```